Website Design Brief for KBR LEGAL PTY LTD

Company Name: KBR LEGAL PTY LTD

Industry: Legal Services

Target Audience:

Corporate clients
Business owners
Individuals seeking legal advice in Commercial Law, Mergers and Acquisitions, Will Law, Property Law, and Conveyancing
Objective:

To create a professional, user-friendly website that establishes trust and authority in the legal field.
Provide easy access to information about the firm’s services, team, and areas of expertise.
Include client testimonials, contact information, and a blog or resource section for legal insights.
Key Features and Pages:

Homepage:

Clean, modern design with a professional feel.
Introduction to KBR LEGAL with a brief overview of services.
High-quality images or illustrations related to law and professionalism.
Prominent call-to-action (CTA) like "Get in Touch" or "Book a Consultation."
About Us:

Information about the firm's mission, values, and team.
Highlight the expertise and experience of key members.
Include a brief company history, if relevant.
Services:

Detailed descriptions of services, categorized by legal areas (e.g., Commercial Law, Mergers & Acquisitions, Property Law, etc.).
Call-to-action buttons to encourage potential clients to reach out for consultations.
Team:

Profiles of key team members, including their qualifications, expertise, and professional photos.
Include links to their professional networks (LinkedIn).
Testimonials:

Section showcasing positive client testimonials or case studies.
This can help build trust and credibility with potential clients.
Blog or Resources:

A blog or resources section providing legal tips, industry news, and insights.
Content should demonstrate the firm’s knowledge and thought leadership.
Contact Us:

Easy-to-use contact form.
Include phone number, email, physical office address, and possibly a map.
Option for booking consultations or initial meetings directly online.
Client Portal (optional):

Secure login for clients to access their case information, documents, and updates (this could be an advanced feature to consider after launch).
Design Aesthetic:

Clean, modern, and professional.
Elegant use of fonts and a color palette that reflects trust, authority, and sophistication (dark blues, whites, grays).
User-friendly navigation to ensure clients can easily find the information they need.
Technical Considerations:

The website should be mobile-responsive and look great on all devices (desktop, tablet, mobile).
Ensure fast load times and optimized images.
Implement SEO best practices to improve search engine rankings.
Easy-to-update CMS (WordPress or similar) to allow easy future updates.
Competitor/Inspirational Websites:

[Provide examples of legal firms' websites you like, or any designs that reflect the feel you want for your firm.]
Additional Information:

Please ensure all content is aligned with the firm's professional tone and approach.
The website should be designed to be scalable for future growth (adding more services, resources, etc.).

Target Market(s)

Business owners Individuals seeking legal advice in Commercial Law, Mergers and Acquisitions, Will Law, Property Law, and Conveyancing

Industry/Entity Type

Legal

Number of Pages Required

3 page

Requirements
Must have
• Home Page, About Us, Contact Us, Services

```html
<!DOCTYPE html>
<html lang="en">
<head>
<meta charset="utf-8">
<title>KBR LEGAL — We Win For You</title>
<link rel="stylesheet" href="https://fonts.googleapis.com/css2?family=Poppins:ital,wght@0,300;0,400;0,500;0,600;0,700;0,800;1,800&family=Lato:wght@400;700&display=swap">
<style>
:root{
  --navy:#0c0a3d;
  --navy-deep:#080628;
  --indigo:#1b1680;
  --purple:#3e35a8;
  --purple-light:#5a50c4;
  --white:#ffffff;
  --ink:#1a1a2e;
  --muted:#4b4b5c;
  --gold:#f5a623;
  --dot:#c9c6ee;
}
*{margin:0;padding:0;box-sizing:border-box}
html,body{width:1200px;height:4785px;overflow:hidden}
body{position:relative;font-family:"Poppins",sans-serif;color:var(--ink);background:var(--white)}
.abs{position:absolute}

/* ---------- header / hero ---------- */
.hero{position:absolute;left:0;top:0;width:1200px;height:660px;overflow:hidden}
.hero-photo{position:absolute;inset:0;background:linear-gradient(180deg,#2c2f6e 0%,#5a4a8a 22%,#d7805a 42%,#f0a45a 50%,#6c5b6a 62%,#2f3b34 78%,#1f2a24 100%)}
.hero-shade{position:absolute;inset:0;background:linear-gradient(90deg,rgba(10,8,40,.55) 0%,rgba(10,8,40,.15) 45%,rgba(0,0,0,0) 70%)}
.topbar-tab{position:absolute;left:585px;top:0;width:240px;height:37px;background:var(--navy);clip-path:polygon(0 0,100% 0,92% 100%,0 100%);color:var(--white);font-size:13px;font-weight:600;line-height:37px;padding-left:40px;clip-path:polygon(8% 0,100% 0,100% 100%,0 100%)}
.topbar-contact{position:absolute;left:790px;top:0;width:410px;height:37px;background:var(--white);clip-path:polygon(9% 0,100% 0,100% 100%,0 100%);font-size:11.5px;font-weight:500;line-height:37px;padding-left:38px;color:var(--ink)}
.topbar-contact strong{font-size:16px;font-weight:600;margin-left:6px}
.brand{position:absolute;left:84px;top:30px;color:var(--white);font-size:44px;font-weight:500;letter-spacing:1px;line-height:52px}
.nav{position:absolute;top:56px;left:526px;display:flex;gap:42px;font-size:14px;font-weight:500;color:var(--white)}
.nav .active{position:relative;font-weight:600}
.nav .active::after{content:"";position:absolute;left:0;right:0;bottom:-5px;height:2px;background:var(--white)}
.hero-kicker{position:absolute;left:110px;top:210px;color:var(--white);font-size:24px;font-weight:700;letter-spacing:3px}
.hero-title{position:absolute;left:108px;top:248px;color:var(--white);font-size:62px;font-weight:800;font-style:italic;letter-spacing:1px;line-height:76px}
.hero-text{position:absolute;left:110px;top:330px;width:410px;color:var(--white);font-size:15px;line-height:26px;font-weight:500}
.btn{display:inline-block;background:var(--navy);color:var(--white);font-weight:700;font-size:14px;letter-spacing:.3px;clip-path:polygon(0 0,100% 0,95% 100%,0 100%)}
.btn-outline{position:absolute;left:115px;top:428px;width:293px;height:48px;border:2px solid var(--white);border-right:none;color:var(--white);font-size:14px;font-weight:700;line-height:44px;padding-left:20px;background:var(--navy);clip-path:polygon(0 0,100% 0,95% 100%,0 100%)}
.hero-edge{position:absolute;left:0;top:0}

/* ---------- section headings ---------- */
.heading{position:absolute;font-size:42px;line-height:50px;color:var(--navy);text-transform:uppercase}
.heading b{font-weight:700}
.heading span{font-weight:400}
.heading::before{content:"";position:absolute;left:0;top:-10px;width:100px;height:6px;background:var(--navy)}
.heading::after{content:"";position:absolute;left:0;bottom:-6px;width:120px;height:3px;background:var(--navy)}
.heading.light{color:var(--white)}
.heading.light::before,.heading.light::after{background:var(--white)}
.kicker{position:absolute;font-size:11px;letter-spacing:1.5px;font-weight:500;color:var(--ink)}
.kicker.light{color:#dcdaf5}

/* ---------- about ---------- */
.about-photo{position:absolute;left:111px;top:740px;width:428px;height:434px;background:linear-gradient(160deg,#b58c5c 0%,#8a6b4a 35%,#2c3142 70%,#1d2230 100%);clip-path:polygon(0 0,92% 0,100% 100%,2% 100%)}
.about-text{position:absolute;left:600px;top:832px;width:488px;font-size:14.3px;line-height:25.6px;color:var(--ink)}
.about-btn{position:absolute;left:600px;top:1128px;width:143px;height:46px;line-height:46px;padding-left:26px}

/* ---------- practice areas ---------- */
.practice{position:absolute;left:0;top:1245px;width:1200px;height:654px}
.practice-bg{position:absolute;inset:0;background:linear-gradient(180deg,#4439b5 0%,#3d33a6 50%,#463cb8 100%);clip-path:polygon(0 128px,100% 10px,100% 100%,0 100%)}
.practice-wedge{position:absolute;left:0;top:0}
.card{position:absolute;top:297px;width:300px;height:279px;background:var(--navy);color:var(--white);text-align:center;padding-top:32px}
.card::before{content:"";position:absolute;left:-4px;top:-3px;width:224px;height:3px;background:var(--white)}
.card::after{content:"";position:absolute;right:-4px;bottom:-4px;width:4px;height:260px;background:var(--white)}
.card .bottom-line{position:absolute;left:74px;bottom:-4px;width:230px;height:4px;background:var(--white)}
.card h3{font-size:18px;font-weight:500;margin-top:18px;letter-spacing:.2px}
.card p{font-size:13px;line-height:26px;color:#dad8ee;margin:10px auto 0;width:250px}
.card .go{display:block;margin:12px auto 0}
.slider-arrow{position:absolute;top:425px}

/* ---------- industries ---------- */
.ind-text{position:absolute;left:110px;top:2100px;width:570px;font-size:14.5px;line-height:25px;color:var(--muted)}
.ind-sub{position:absolute;left:110px;top:2168px;font-size:19px;font-weight:500;color:var(--ink)}
.ind-item{position:absolute;left:110px;width:560px;height:80px}
.ind-item .dia{position:absolute;left:4px;top:2px;width:58px;height:58px;background:var(--navy);transform:rotate(45deg);outline:2px solid var(--white);outline-offset:-5px}
.ind-item svg{position:absolute;left:18px;top:16px}
.ind-item h4{position:absolute;left:96px;top:0;font-size:13.5px;font-weight:600;color:var(--ink)}
.ind-item p{position:absolute;left:96px;top:20px;font-size:13px;line-height:20px;color:var(--muted);width:460px}
.ind-btn{position:absolute;left:111px;top:2531px;width:150px;height:45px;line-height:45px;padding-left:22px}
.collage{position:absolute;left:715px;top:1973px;width:485px;height:602px}

/* ---------- success stories ---------- */
.stories{position:absolute;left:0;top:2648px;width:1200px;height:737px;background:linear-gradient(170deg,#2a2296 0%,#3b32a7 40%,#2f27a0 70%,#1a1480 100%)}
.story{position:absolute;top:282px;width:312px}
.story .thumb{width:312px;height:234px}
.story .date{margin-top:18px;font-size:11.5px;color:#dcdaf5;border-left:3px solid var(--white);padding-left:14px;line-height:14px;margin-left:0}
.story h3{margin:12px 0 0 16px;font-size:17px;line-height:28px;font-weight:500;color:var(--white)}
.story .more{margin:14px 0 0 16px;font-size:13px;font-weight:600;color:var(--white)}

/* ---------- testimonials ---------- */
.avatar{position:absolute;border-radius:50%}
.t-name{position:absolute;left:0;width:1200px;top:3762px;text-align:center;font-size:19px;font-weight:600;letter-spacing:.5px;color:var(--ink)}
.t-place{position:absolute;left:0;width:1200px;top:3802px;text-align:center;font-size:11px;color:#777;font-family:"Lato",sans-serif}
.t-stars{position:absolute;left:0;width:1200px;top:3830px;text-align:center;color:var(--gold);font-size:28px;letter-spacing:1px;line-height:32px}
.t-quote{position:absolute;left:270px;width:660px;top:3874px;text-align:center;font-family:"Lato",sans-serif;font-size:14.5px;line-height:26px;color:#3a3a48}
.dots{position:absolute;left:552px;top:3985px;display:flex;gap:8px}
.dots i{display:block;width:13px;height:13px;border-radius:50%;background:var(--dot)}
.dots i.on{background:var(--navy)}

/* ---------- footer ---------- */
.footer{position:absolute;left:0;top:4020px;width:1200px;height:765px}
.footer-bg{position:absolute;inset:0;background:var(--navy-deep);clip-path:polygon(0 130px,100% 10px,100% 100%,0 100%)}
.footer-brand{position:absolute;left:0;width:1200px;top:250px;text-align:center;color:var(--white);font-size:74px;font-weight:500;letter-spacing:2px;line-height:80px}
.footer-nav{position:absolute;left:0;width:1200px;top:385px;display:flex;justify-content:center;gap:42px;color:var(--white);font-size:15px;font-weight:500}
.contact-box{position:absolute;left:111px;top:454px;width:978px;height:115px;border:1px solid #6b6999;background:#100e3f;display:flex}
.contact-item{flex:1;position:relative;padding:32px 0 0 72px;color:var(--white)}
.contact-item+.contact-item::before{content:"";position:absolute;left:0;top:16px;bottom:16px;width:1px;background:#4a4880}
.contact-item .ic{position:absolute;left:18px;top:34px}
.contact-item h5{font-size:14px;font-weight:500;letter-spacing:.3px}
.contact-item p{font-size:13.5px;margin-top:4px;color:#dcdaf5}
.legal-links{position:absolute;left:0;width:1200px;top:607px;text-align:center;color:var(--white);font-size:15px}
.legal-links span{margin:0 28px}
.copyright{position:absolute;left:0;width:1200px;top:680px;text-align:center;color:var(--white);font-size:14px}
</style>
</head>
<body>

<!-- ================= HERO ================= -->
<header class="hero">
  <div class="hero-photo" role="img" aria-label="City skyline at sunset with palm trees and highway"></div>
  <div class="hero-shade"></div>
  <div class="topbar-tab">CONNECT WITH US</div>
  <div class="topbar-contact">CONTACT US TODAY: <strong>+1 555 010 2040</strong></div>
  <div class="brand">KBR LEGAL</div>
  <nav class="nav">
    <span class="active">HOME</span><span>ABOUT</span><span>PRACTICE AREAS</span><span>TESTIMONIALS</span><span>BLOG</span>
  </nav>
  <div class="hero-kicker">KBR LEGAL</div>
  <h1 class="hero-title">WE WIN FOR YOU</h1>
  <p class="hero-text">Lorem ipsum dolor sit amet, consectetur adipiscing elit, sed do eiusmod tempor incididunt ut labore et dolore magna aliqua.</p>
  <div class="btn-outline">REQUEST A FREE CONSULTATION</div>
  <svg class="hero-edge" width="1200" height="660" viewBox="0 0 1200 660" aria-hidden="true">
    <polygon points="0,641 1200,522 1200,660 0,660" fill="#ffffff"/>
    <polygon points="743,563 1200,532 1200,645" fill="#0c0a3d"/>
    <circle cx="600" cy="576" r="19" fill="#ffffff" stroke="#0c0a3d" stroke-width="2.5"/>
    <path d="M600 566v18M592 577l8 8 8-8" fill="none" stroke="#0c0a3d" stroke-width="2.5" stroke-linecap="round" stroke-linejoin="round"/>
  </svg>
</header>

<!-- ================= ABOUT ================= -->
<section class="about">
  <div class="about-photo" role="img" aria-label="Smiling lawyer in a suit standing in an office"></div>
  <h2 class="heading" style="left:600px;top:733px"><b>ABOUT KBR</b> <span>LEGAL</span></h2>
  <div class="kicker" style="left:600px;top:808px">WHO WE ARE</div>
  <p class="about-text">Lorem ipsum dolor sit amet, consectetur adipiscing elit, sed do eiusmod tempor incididunt ut labore et dolore magna Duis aute irure dolor in reprehenderit in voluptate velit esse cillum dolore eu fugiat nulla pariatur. Excepteur sint occaecat cupid atat non proint, sunt in culpa qui officia deserunt mollit anm id est aliqua. Ut enim ad minim veniam, quis nostrud exerc iatn ullamco laboris nisi ut aliquip ex ea commodo conse quat. Dui aute irure dolor in eiusm cat cupiat officia deseruntod tempor incididunt ut labore et dolore magna Duisrepreh enderit in voluptate velit esse cillum dolore eu fugiat nulla pariatur. Excepteur sint occaecat cupiat officia deserunt mollit anim id est laborum.</p>
  <div class="btn about-btn">READ MORE</div>
</section>

<!-- ================= PRACTICE AREAS ================= -->
<section class="practice">
  <div class="practice-bg" role="img" aria-label="Classical courthouse columns in blue tone"></div>
  <svg class="practice-wedge" width="1200" height="140" viewBox="0 0 1200 140" aria-hidden="true">
    <polygon points="0,0 490,78 0,120" fill="#0c0a3d"/>
    <polygon points="600,70 1200,0 1200,16 620,80" fill="#0c0a3d"/>
  </svg>
  <h2 class="heading light" style="left:437px;top:172px"><b>PRACTICE</b> <span>AREAS</span></h2>
  <div class="kicker light" style="left:0;width:1200px;text-align:center;top:253px">WHAT WE OFFER</div>

  <svg class="slider-arrow" style="left:42px" width="28" height="28" viewBox="0 0 28 28" aria-hidden="true"><circle cx="14" cy="14" r="12" fill="#7a72c8"/><path d="M17 14H10M13 10l-4 4 4 4" fill="none" stroke="#3e35a8" stroke-width="2" stroke-linecap="round" stroke-linejoin="round"/></svg>
  <svg class="slider-arrow" style="left:1131px" width="28" height="28" viewBox="0 0 28 28" aria-hidden="true"><circle cx="14" cy="14" r="12" fill="#ffffff"/><path d="M10 14h7M15 10l4 4-4 4" fill="none" stroke="#0c0a3d" stroke-width="2" stroke-linecap="round" stroke-linejoin="round"/></svg>

  <article class="card" style="left:111px">
    <svg width="48" height="50" viewBox="0 0 48 50" aria-hidden="true"><rect x="14" y="4" width="26" height="36" rx="2" fill="none" stroke="#fff" stroke-width="3"/><path d="M20 14h14M20 21h14M20 28h10" stroke="#fff" stroke-width="2.5"/><rect x="6" y="30" width="12" height="14" fill="#fff"/></svg>
    <h3>COMMERCIAL LAW</h3>
    <p>Excepteur sint occaecat cupidatat non proident, sunt in culpa qui officia deserunt</p>
    <svg class="go" width="18" height="18" viewBox="0 0 18 18" aria-hidden="true"><circle cx="9" cy="9" r="8" fill="#fff"/><path d="M6 9h6M10 6l3 3-3 3" fill="none" stroke="#0c0a3d" stroke-width="2"/></svg>
    <span class="bottom-line"></span>
  </article>
  <article class="card" style="left:448px">
    <svg width="54" height="50" viewBox="0 0 54 50" aria-hidden="true"><path d="M20 44V20M20 24c-8 0-12-6-12-12 8 0 12 5 12 12zM20 20c0-8 5-12 12-12 0 7-5 12-12 12" fill="#fff"/><rect x="6" y="40" width="28" height="6" fill="#fff"/><circle cx="38" cy="32" r="11" fill="#fff"/><text x="38" y="37" text-anchor="middle" font-family="Poppins,sans-serif" font-size="14" font-weight="700" fill="#0c0a3d">$</text></svg>
    <h3>MERGERS &amp; ACQUISITIONS</h3>
    <p>Excepteur sint occaecat cupidatat non proident, sunt in culpa qui officia deserunt</p>
    <svg class="go" width="18" height="18" viewBox="0 0 18 18" aria-hidden="true"><circle cx="9" cy="9" r="8" fill="#fff"/><path d="M6 9h6M10 6l3 3-3 3" fill="none" stroke="#0c0a3d" stroke-width="2"/></svg>
    <span class="bottom-line"></span>
  </article>
  <article class="card" style="left:790px">
    <svg width="46" height="50" viewBox="0 0 46 50" aria-hidden="true"><rect x="8" y="4" width="30" height="40" rx="2" fill="none" stroke="#fff" stroke-width="3"/><path d="M15 20l8-7 8 7v9H15z" fill="#fff"/><path d="M14 36h18" stroke="#fff" stroke-width="2.5"/></svg>
    <h3>PROPERTY LAW</h3>
    <p>Excepteur sint occaecat cupidatat non proident, sunt in culpa qui officia deserunt</p>
    <svg class="go" width="18" height="18" viewBox="0 0 18 18" aria-hidden="true"><circle cx="9" cy="9" r="8" fill="#fff"/><path d="M6 9h6M10 6l3 3-3 3" fill="none" stroke="#0c0a3d" stroke-width="2"/></svg>
    <span class="bottom-line"></span>
  </article>
</section>

<!-- ================= INDUSTRIES ================= -->
<section class="industries">
  <h2 class="heading" style="left:110px;top:1996px"><b>INDUSTRIES</b> <span>WE SERVED</span></h2>
  <div class="kicker" style="left:110px;top:2074px">HARROW TRIAL GROUP PLLC</div>
  <p class="ind-text">Lorem ipsum dolor sit amet, consectetur adipiscing elit, sed do eiusmod si ut aliquip ex ea commodo consequat eu fugiat nulla pariatur.</p>
  <div class="ind-sub">The Law Firm Specializes in</div>

  <div class="ind-item" style="top:2216px">
    <span class="dia"></span>
    <svg width="34" height="34" viewBox="0 0 34 34" aria-hidden="true"><circle cx="17" cy="17" r="9" fill="none" stroke="#fff" stroke-width="2.5"/><circle cx="17" cy="17" r="3" fill="#fff"/></svg>
    <h4>COUNSELING AND REPRESENTING LARGE CORPORATIONS</h4>
    <p>Duis aute irure dolor in reprehenderit in voluptate velit esse cillum dolore eu fugiat nulla pariatur.</p>
  </div>
  <div class="ind-item" style="top:2312px">
    <span class="dia"></span>
    <svg width="34" height="34" viewBox="0 0 34 34" aria-hidden="true"><rect x="8" y="9" width="18" height="16" fill="none" stroke="#fff" stroke-width="2.5"/><path d="M8 14h18M13 19h3M19 19h3" stroke="#fff" stroke-width="2"/></svg>
    <h4>SMALL BUSINESSES AND ENTREPRENEURS</h4>
    <p>Duis aute irure dolor in reprehenderit in voluptate velit esse cillum dolore eu fugiat nulla pariatur.</p>
  </div>
  <div class="ind-item" style="top:2416px">
    <span class="dia"></span>
    <svg width="34" height="34" viewBox="0 0 34 34" aria-hidden="true"><path d="M12 14l6-6 4 4-6 6z" fill="#fff"/><rect x="8" y="22" width="18" height="5" fill="#fff"/></svg>
    <h4>OUT OF THE COURTROOM</h4>
    <p>Duis aute irure dolor in reprehenderit in voluptate velit esse cillum dolore eu fugiat nulla pariatur.</p>
  </div>

  <div class="btn ind-btn">GET STARTED</div>

  <svg class="collage" width="485" height="602" viewBox="0 0 485 602" role="img" aria-label="Collage of diamond-shaped photos: smiling shop owner, colleagues at a laptop, glass office towers and a business handshake">
    <defs>
      <linearGradient id="gA" x1="0" y1="0" x2="0" y2="1"><stop offset="0" stop-color="#c9a889"/><stop offset="1" stop-color="#5b6a86"/></linearGradient>
      <linearGradient id="gB" x1="0" y1="0" x2="1" y2="1"><stop offset="0" stop-color="#8a7a6a"/><stop offset="1" stop-color="#3f4a5a"/></linearGradient>
      <linearGradient id="gC" x1="0" y1="0" x2="1" y2="1"><stop offset="0" stop-color="#9cc1e0"/><stop offset="1" stop-color="#24446e"/></linearGradient>
      <linearGradient id="gD" x1="0" y1="0" x2="0" y2="1"><stop offset="0" stop-color="#c6b6a4"/><stop offset="1" stop-color="#2b2f40"/></linearGradient>
    </defs>
    <polygon points="297,0 440,143 297,286 154,143" fill="url(#gA)"/>
    <polygon points="157,135 297,275 157,415 17,275" fill="url(#gB)"/>
    <polygon points="445,150 485,135 485,420 345,280" fill="url(#gC)"/>
    <polygon points="298,285 455,442 298,600 141,442" fill="url(#gD)"/>
  </svg>
</section>

<!-- ================= SUCCESS STORIES ================= -->
<section class="stories">
  <div class="abs" style="inset:0" role="img" aria-label="Courthouse columns in deep blue tone"></div>
  <svg class="abs" style="left:0;top:0" width="1200" height="130" viewBox="0 0 1200 130" aria-hidden="true">
    <polygon points="0,0 1200,0 1200,30 0,0" fill="#ffffff"/>
    <polygon points="706,65 1200,28 1200,110" fill="#0c0a3d"/>
    <polygon points="706,65 1200,100 1200,116 690,70" fill="#ffffff"/>
  </svg>
  <h2 class="heading light" style="left:414px;top:155px"><b>SUCCESS</b> <span>STORIES</span></h2>
  <div class="kicker light" style="left:0;width:1200px;text-align:center;top:228px">BLOG</div>

  <article class="story" style="left:111px">
    <div class="thumb" role="img" aria-label="Colleagues meeting around a laptop in a bright office" style="background:linear-gradient(135deg,#c7ccd3 0%,#8d8f95 50%,#3e3e48 100%)"></div>
    <div class="date">18 Jan 2025</div>
    <h3>Lorem ipsum dolor sit amet, con sectetur adipiscing elit</h3>
    <div class="more">LEARN MORE</div>
  </article>
  <article class="story" style="left:444px">
    <div class="thumb" role="img" aria-label="Looking up at tall stone courthouse columns under blue sky" style="background:linear-gradient(180deg,#4f8fd1 0%,#9fb9d1 45%,#cfd2d3 75%,#8a8f95 100%)"></div>
    <div class="date">15 Jan 2025</div>
    <h3>Lorem ipsum dolor sit amet, con sectetur adipiscing elit</h3>
    <div class="more">LEARN MORE</div>
  </article>
  <article class="story" style="left:777px">
    <div class="thumb" role="img" aria-label="Hands signing a contract on a wooden desk" style="background:linear-gradient(160deg,#e2dfdb 0%,#b29f8a 50%,#6d5843 100%)"></div>
    <div class="date">12 Jan 2025</div>
    <h3>Lorem ipsum dolor sit amet, con sectetur adipiscing elit</h3>
    <div class="more">LEARN MORE</div>
  </article>
</section>

<!-- ================= TESTIMONIALS ================= -->
<section class="testimonials">
  <h2 class="heading" style="left:352px;top:3470px"><b>WHAT CUSTOMER</b> <span>SAYS</span></h2>
  <div class="kicker" style="left:0;width:1200px;text-align:center;top:3547px">TESTIMONIALS</div>

  <div class="avatar" style="left:533px;top:3602px;width:134px;height:134px;border:3px solid var(--navy);padding:6px">
    <div style="width:100%;height:100%;border-radius:50%;background:linear-gradient(180deg,#f3a766,#d67b3d)" role="img" aria-label="Client portrait"></div>
  </div>
  <div class="avatar" role="img" aria-label="Client portrait" style="left:1016px;top:3614px;width:44px;height:44px;background:linear-gradient(180deg,#b8b8c0,#5d5d68)"></div>
  <div class="avatar" role="img" aria-label="Client portrait" style="left:138px;top:3687px;width:66px;height:66px;background:linear-gradient(180deg,#e8c9b2,#a57a62)"></div>
  <div class="avatar" style="left:381px;top:3724px;width:14px;height:14px;background:var(--indigo)"></div>
  <div class="avatar" style="left:898px;top:3688px;width:7px;height:7px;background:var(--ink)"></div>

  <div class="t-name">DANIEL WHITMORE</div>
  <div class="t-place">United States</div>
  <div class="t-stars">★★★★★</div>
  <svg class="abs" style="left:170px;top:3783px" width="100" height="85" viewBox="0 0 100 85" aria-hidden="true"><path d="M4 80V45C4 20 14 6 38 2v14C24 20 20 30 20 42h20v38zM56 80V45C56 20 66 6 90 2v14C76 20 72 30 72 42h20v38z" fill="#d9d9de"/></svg>
  <p class="t-quote">Temporibus aaut rerum necessitatibus saepe eveniet ut et voluptates repudiandae sint et molestiae non recusandae. Itaque earum rerum hic tenetur a sapiente delectus, ut aut reiciendis voluptatibus maiores alias consequatur aut perferendis doloribus asperiores repellat.</p>
  <svg class="abs" style="left:957px;top:3888px" width="100" height="85" viewBox="0 0 100 85" aria-hidden="true"><path d="M96 5v35c0 25-10 39-34 43V69c14-4 18-14 18-26H60V5zM44 5v35c0 25-10 39-34 43V69c14-4 18-14 18-26H8V5z" fill="#d9d9de"/></svg>
  <div class="dots"><i></i><i></i><i></i><i class="on"></i><i></i><i></i></div>
</section>

<!-- ================= FOOTER ================= -->
<footer class="footer">
  <svg class="abs" style="left:0;top:0" width="1200" height="140" viewBox="0 0 1200 140" aria-hidden="true">
    <polygon points="0,0 1200,10 0,110" fill="#1b1680"/>
  </svg>
  <div class="footer-bg"></div>
  <div class="footer-brand">KBR LEGAL</div>
  <nav class="footer-nav"><span>HOME</span><span>ABOUT</span><span>PRACTICE AREAS</span><span>TESTIMONIALS</span><span>BLOG</span><span>CONTACT US</span></nav>

  <div class="contact-box">
    <div class="contact-item">
      <svg class="ic" width="40" height="40" viewBox="0 0 40 40" aria-hidden="true"><circle cx="20" cy="20" r="19" fill="#fff"/><path d="M20 10c-4.4 0-8 3.4-8 7.6C12 23 20 30 20 30s8-7 8-12.4C28 13.4 24.4 10 20 10z" fill="#1b1680"/><circle cx="20" cy="17.5" r="3" fill="#fff"/></svg>
      <h5>ADDRESS</h5><p>KBR Legal, United States</p>
    </div>
    <div class="contact-item">
      <svg class="ic" width="40" height="40" viewBox="0 0 40 40" aria-hidden="true"><circle cx="20" cy="20" r="19" fill="#fff"/><path d="M14 11l4 1 1.5 5-2.5 2c1 2.5 3 4.5 5.5 5.5l2-2.5 5 1.5 1 4c-1 2-3 3-5 3-8 0-15-7-15-15 0-2 1-4 3.5-4.5z" fill="#1b1680"/></svg>
      <h5>PHONE</h5><p>+1 555 010 2040</p>
    </div>
    <div class="contact-item">
      <svg class="ic" width="40" height="40" viewBox="0 0 40 40" aria-hidden="true"><circle cx="20" cy="20" r="19" fill="#fff"/><rect x="12" y="16" width="16" height="12" rx="1.5" fill="#1b1680"/><rect x="15" y="11" width="10" height="6" fill="none" stroke="#1b1680" stroke-width="2"/><path d="M15 21h10M15 24h6" stroke="#fff" stroke-width="1.5"/></svg>
      <h5>FAX</h5><p>+1 555 010 2041</p>
    </div>
    <div class="contact-item">
      <svg class="ic" width="40" height="40" viewBox="0 0 40 40" aria-hidden="true"><circle cx="20" cy="20" r="19" fill="#fff"/><rect x="11" y="13" width="18" height="14" rx="1.5" fill="#1b1680"/><path d="M11 14l9 7 9-7" fill="none" stroke="#fff" stroke-width="1.6"/></svg>
      <h5>EMAIL</h5><p>info@kbrlegal.com</p>
    </div>
  </div>

  <div class="legal-links"><span>Privacy Policy</span>|<span>Terms &amp; Conditions</span>|<span>Support Links</span>|<span>Contact Us</span></div>
  <div class="copyright">Copyrights@2025.KBR Legal.All Rights Reserverd</div>
</footer>

</body>
</html>
```